Marrowind Lake Billboard

Looking to design a multi purpose billboard promoting Marrowind Lake as a destination point. Billboard size is 12ft x 40ft
My goal is to advertise our restaurant The Driftmill (pic attached)
What makes Marrowind a destination? It offers lodging / water skiing / Off Road Adventure / Camping / Fishing / Hunting
Want a catch phrase, something like "Looking For a Getaway" or "Need a Break"
Needs to really pop and catch the interest of the looker
maybe have our website address www.marrowinddriftmill.example
Open for ideas

```html
<!DOCTYPE html>
<html lang="en">
<head>
<meta charset="utf-8">
<title>Marrowind Lake Billboard</title>
<link rel="stylesheet" href="https://fonts.googleapis.com/css2?family=Mr+Dafoe&family=Ultra&family=League+Spartan:wght@600;700;800&display=swap">
<style>
  :root {
    --page: #ffffff;
    --board: #111111;
    --ink: #ffffff;
    --peach: #f6a571;
    --peach-shadow: #111111;
    --sky-top: #5b6d9c;
    --sky-mid: #8d94bd;
    --sunset: #e6707a;
    --lake: #2c2d3f;
    --store-warm: #a4581e;
    --store-dark: #2a1a0f;
    --ribs: #b14a1c;
    --wrap: #d9b890;
  }
  * { margin: 0; padding: 0; box-sizing: border-box; }
  html, body { width: 1200px; height: 444px; overflow: hidden; background: var(--page); }
  .canvas { position: relative; width: 1200px; height: 444px; background: var(--page); }
  .billboard {
    position: absolute; left: 48px; top: 59px; width: 1105px; height: 331px;
    background: var(--board); overflow: hidden;
  }
  .lake-scene {
    position: absolute; left: 742px; top: 0; width: 363px; height: 331px;
    background: linear-gradient(180deg, var(--sky-top) 0%, var(--sky-mid) 38%, var(--sunset) 58%, #b8596a 66%, var(--lake) 100%);
  }
  .photo-circle {
    position: absolute; border-radius: 50%; border: 5px solid var(--board);
  }
  .photo-circle--store {
    left: 590px; top: 8px; width: 320px; height: 320px;
    background: radial-gradient(circle at 55% 55%, #d4893d 0%, var(--store-warm) 35%, #5a3316 65%, var(--store-dark) 100%);
  }
  .photo-circle--ribs {
    left: 570px; top: 212px; width: 104px; height: 104px;
    background: radial-gradient(circle at 50% 60%, #d46a2c 0%, var(--ribs) 45%, #3a1a0c 100%);
  }
  .photo-circle--wrap {
    left: 807px; top: 161px; width: 148px; height: 148px;
    background: radial-gradient(circle at 55% 55%, #b8433a 0%, #7f8a3c 30%, var(--wrap) 60%, #c9a06e 100%);
  }
  .headline-script {
    position: absolute; left: 42px; top: 14px;
    font-family: "Mr Dafoe", cursive; font-size: 84px; line-height: 1;
    color: var(--ink); transform: rotate(-4deg); transform-origin: left bottom;
    white-space: nowrap; z-index: 2;
  }
  .headline-main {
    position: absolute; left: 24px; top: 96px;
    font-family: "Ultra", serif; font-size: 70px; line-height: 1;
    letter-spacing: -1px; color: var(--peach);
    text-shadow: 3px 3px 0 var(--peach-shadow), 5px 5px 0 var(--peach);
    white-space: nowrap;
  }
  .question {
    position: absolute; left: 27px; top: 185px;
    font-family: "League Spartan", sans-serif; font-weight: 700;
    font-size: 23px; line-height: 1; color: var(--ink); white-space: nowrap;
  }
  .offers {
    position: absolute; left: 25px; top: 212px;
    font-family: "League Spartan", sans-serif; font-weight: 700;
    font-size: 12px; line-height: 1; color: var(--ink); white-space: nowrap;
  }
  .offers .chevrons { color: var(--peach); letter-spacing: -2px; margin-right: 3px; }
  .offers .activity { color: var(--peach); }
  .brand-mark {
    position: absolute; left: 25px; top: 296px;
    display: flex; align-items: center; gap: 5px;
    font-family: "League Spartan", sans-serif; font-weight: 700;
    font-size: 10px; color: var(--ink); white-space: nowrap;
  }
  .brand-mark .dot { width: 12px; height: 12px; border-radius: 50%; border: 1.5px solid var(--ink); }
  .website {
    position: absolute; left: 345px; top: 302px;
    font-family: "League Spartan", sans-serif; font-weight: 700;
    font-size: 9.5px; letter-spacing: 2.4px; color: var(--ink); white-space: nowrap;
  }
</style>
</head>
<body>
<div class="canvas">
  <section class="billboard">
    <div class="lake-scene" role="img" aria-label="Sunset over the lake with blue and pink sky reflected in the water"></div>
    <div class="photo-circle photo-circle--store" role="img" aria-label="The Driftmill general store and bait shop front lit warmly at dusk"></div>
    <div class="photo-circle photo-circle--ribs" role="img" aria-label="Racks of ribs smoking on a grill"></div>
    <div class="photo-circle photo-circle--wrap" role="img" aria-label="Grilled wrap filled with meat, lettuce and tomato"></div>

    <div class="headline-script">Looking For a</div>
    <h1 class="headline-main">GETAWAY</h1>
    <h2 class="question">WHAT MAKES MARROWIND A DESTINATION?</h2>
    <p class="offers"><span class="chevrons">&#8250;&#8250;&#8250;</span>IT OFFERS <span class="activity">LODGING / WATER SKIING / OFF ROAD ADVENTURE / CAMPING / FISHING / HUNTING</span></p>

    <div class="brand-mark"><span class="dot"></span>The Driftmill</div>
    <p class="website">WWW.MARROWINDDRIFTMILL.EXAMPLE</p>
  </section>
</div>
</body>
</html>
```